Varnell Skyworks Limited

Started a consulting business 12 months ago and have since moved location and have grown and seek to identify my self to the industry.
Specializing in quality solutions, business documentation and maintenance solution's

Industry/Entity Type

Business

```html
<!DOCTYPE html>
<html lang="en">
<head>
<meta charset="utf-8">
<title>Varnell Skyworks Limited – Business Card</title>
<link rel="stylesheet" href="https://fonts.googleapis.com/css2?family=Crimson+Text:wght@400&display=swap">
<style>
  :root {
    --backdrop: #e9e4dc;
    --card: #6f5b41;
    --card-light: #8a7558;
    --card-dark: #4a3b28;
    --ink: #1f170f;
    --rule: #2a2016;
  }
  * { margin: 0; padding: 0; box-sizing: border-box; }
  html, body {
    width: 1200px;
    height: 1000px;
    overflow: hidden;
    background: var(--backdrop);
  }
  .canvas {
    width: 1200px;
    height: 1000px;
    display: flex;
    align-items: center;
    justify-content: center;
  }
  .business-card {
    width: 900px;
    height: 514px;
    background: var(--card);
    box-shadow: 0 10px 30px rgba(0,0,0,0.18);
    font-family: "Crimson Text", "Times New Roman", serif;
    color: var(--ink);
    position: relative;
  }
  .company-name {
    position: absolute;
    top: 62px;
    left: 0;
    right: 0;
    text-align: center;
    font-size: 64px;
    font-weight: 400;
    letter-spacing: 1px;
    color: var(--card);
    text-shadow:
      -1px -1px 0 var(--card-dark),
      1px 1px 0 var(--card-light),
      2px 2px 1px rgba(255,255,255,0.08);
  }
  .person-name {
    position: absolute;
    top: 215px;
    left: 0;
    right: 0;
    text-align: center;
    font-size: 26px;
  }
  .details {
    position: absolute;
    top: 280px;
    left: 0;
    right: 0;
    display: flex;
    justify-content: center;
    font-size: 19px;
    line-height: 1.55;
  }
  .address {
    width: 380px;
    text-align: right;
    padding-right: 22px;
  }
  .divider {
    width: 1px;
    height: 104px;
    background: var(--rule);
  }
  .contact {
    width: 380px;
    text-align: left;
    padding-left: 22px;
    padding-top: 14px;
  }
</style>
</head>
<body>
  <main class="canvas">
    <section class="business-card">
      <h1 class="company-name">Varnell Skyworks Limited</h1>
      <p class="person-name">Martin R Hale</p>
      <div class="details">
        <address class="address" style="font-style: normal;">
          Unit B014, 12 Carrow Road<br>
          Westfield Park 2041<br>
          Northbridge NZ
        </address>
        <div class="divider"></div>
        <div class="contact">
          Mobile +64 21 555 014<br>
          Email : info@varnellsky.co.nz
        </div>
      </div>
    </section>
  </main>
</body>
</html>
```